FinServices firm business card
Business card design
Project: FinServices firm business card
FinServices firm business card -
Creative Brief
Use specific fonts
Close to logo, but use whatever makes it look better.
Traditional
Ravindra Kohli
Managing Partner
214 Lantern Avenue, 12th Floor Boston, MA 02187
rkohli@dorvenpartners.example
www.dorvenpartners.example
Please suggest options.. as we have multiple offices and would like to highlight other locations (not addresses). Also, we could twitter, etc.. on back page.. please advise what is norm.

```html
<!DOCTYPE html>
<html lang="en">
<head>
<meta charset="utf-8">
<title>Dorven Partners — Stationery</title>
<link href="https://fonts.googleapis.com/css2?family=Open+Sans:wght@400;600;700&display=swap" rel="stylesheet">
<style>
  :root{
    --navy:#1c3766;
    --navy-deep:#142a52;
    --grey-light:#f4f4f4;
    --grey-mid:#dcdcdc;
    --grey-strip:#c9ccd1;
    --ink:#3a3f47;
    --muted:#7b818a;
    --paper:#ffffff;
    --backdrop:#e8e5df;
  }
  *{box-sizing:border-box;margin:0;padding:0}
  html,body{width:1200px;height:785px;overflow:hidden}
  body{background:var(--backdrop);font-family:"Open Sans",Arial,sans-serif;color:var(--ink);position:relative}

  .wordmark{font-family:"Open Sans",Arial,sans-serif;font-weight:700;color:var(--navy);line-height:1;text-align:center;letter-spacing:.04em}
  .wordmark .line{display:block}
  .mark-dot{border-radius:50%;background:var(--navy)}

  /* Business cards */
  .card{position:absolute;left:96px;width:288px;height:187px;border-radius:8px;overflow:hidden;box-shadow:0 2px 6px rgba(0,0,0,.18)}
  .card--front{background:linear-gradient(90deg,var(--paper) 0%,var(--grey-light) 45%,var(--grey-mid) 100%)}
  .card--a{top:96px}
  .card--b{top:293px}
  .card--back{top:492px;background:var(--navy)}
  .card__brand{position:absolute;left:18px;top:34px;width:88px;display:flex;flex-direction:column;align-items:center}
  .card__brand .mark-dot{width:30px;height:30px;margin-bottom:6px}
  .card__brand .wordmark{font-size:17px}
  .card__brand .wordmark .line+.line{font-size:9px;letter-spacing:.32em;margin-top:3px}
  .card__divider{position:absolute;left:116px;top:22px;width:1px;height:120px;background:#b9bcc1}
  .card__person{position:absolute;left:128px;top:26px;font-size:7px;line-height:1.45;color:var(--muted)}
  .card__name{font-size:10px;font-weight:700;color:var(--ink)}
  .card__title{font-size:7px;margin-bottom:10px}
  .card__gap{margin-top:8px}
  .card__band{position:absolute;left:0;right:0;bottom:0;height:22px;background:var(--navy)}
  .card__band::before{content:"";position:absolute;left:0;top:-5px;width:136px;height:5px;background:var(--grey-strip)}
  .card__slashes{position:absolute;left:132px;top:-5px}
  .card__url{position:absolute;right:14px;top:0;height:22px;display:flex;align-items:center;font-size:7px;font-weight:600;color:#fff;letter-spacing:.04em}
  .card--back .faint{position:absolute;left:20px;top:20px;width:130px;height:130px;border-radius:50%;background:rgba(255,255,255,.06)}
  .card--back .back-brand{position:absolute;left:170px;top:70px;display:flex;flex-direction:column;align-items:center}
  .card--back .mark-dot{width:34px;height:34px;background:#fff}
  .card--back .url{position:absolute;right:16px;bottom:14px;font-size:7px;color:#dfe5ef}

  /* Letterhead */
  .sheet{position:absolute;background:var(--paper);box-shadow:0 2px 6px rgba(0,0,0,.15)}
  .sheet--under{left:430px;top:104px;width:283px;height:560px;transform:rotate(1.2deg)}
  .letterhead{left:420px;top:96px;width:283px;height:560px}
  .letterhead__brand{position:absolute;left:20px;top:24px;display:flex;flex-direction:column;align-items:center}
  .letterhead__brand .mark-dot{width:24px;height:24px;margin-bottom:4px}
  .letterhead__brand .wordmark{font-size:13px}
  .letterhead__brand .wordmark .line+.line{font-size:7px;letter-spacing:.3em;margin-top:2px}
  .letterhead__contact{position:absolute;right:18px;top:26px;font-size:5px;line-height:1.5;color:var(--muted);text-align:left}
  .letterhead .faint{position:absolute;left:60px;top:200px;width:170px;height:170px;border-radius:50%;background:#f3f4f6}
  .letterhead__foot{position:absolute;left:0;right:0;bottom:0;height:12px;background:var(--navy);font-size:5px;color:#fff;display:flex;align-items:center;justify-content:flex-end;padding-right:12px}

  /* Envelope */
  .envelope-back{position:absolute;left:672px;top:318px;width:420px;height:168px;background:var(--paper);transform:rotate(-5deg);box-shadow:0 2px 6px rgba(0,0,0,.15);overflow:hidden}
  .envelope-back svg{position:absolute;left:0;top:0}
  .envelope-back .mark-dot{position:absolute;left:196px;top:36px;width:28px;height:28px;background:#fff}
  .envelope{position:absolute;left:696px;top:365px;width:402px;height:175px;background:var(--paper);box-shadow:0 2px 6px rgba(0,0,0,.2);overflow:hidden}
  .envelope__brand{position:absolute;left:14px;top:16px;display:flex;flex-direction:column;align-items:center;width:60px}
  .envelope__brand .mark-dot{width:18px;height:18px;margin-bottom:3px}
  .envelope__brand .wordmark{font-size:10px}
  .envelope__brand .wordmark .line+.line{font-size:5px;letter-spacing:.28em;margin-top:2px}
  .envelope__address{position:absolute;left:14px;top:72px;font-size:5px;color:var(--muted)}
  .envelope .faint{position:absolute;left:220px;top:20px;width:150px;height:150px;border-radius:50%;background:#f2f3f5}
  .envelope__foot{position:absolute;left:0;right:0;bottom:0;height:12px;background:var(--navy);font-size:5px;color:#fff;display:flex;align-items:center;justify-content:flex-end;padding-right:12px}
</style>
</head>
<body>

<!-- Business card, front -->
<section class="card card--front card--a">
  <div class="card__brand">
    <div class="mark-dot"></div>
    <div class="wordmark"><span class="line">DORVEN</span><span class="line">PARTNERS</span></div>
  </div>
  <div class="card__divider"></div>
  <div class="card__person">
    <div class="card__name">Ravindra Kohli</div>
    <div class="card__title">Managing Partner</div>
    <div>214 Lantern Avenue, 12th Floor</div>
    <div>Boston, MA 02187</div>
    <div class="card__gap">Phone +1 617 555 0142</div>
    <div>Fax +1 617 555 0143</div>
    <div>Email rkohli@dorvenpartners.example</div>
  </div>
  <div class="card__band">
    <svg class="card__slashes" width="20" height="27" viewBox="0 0 20 27" aria-hidden="true"><path d="M4 0h5L3 27H-2z" fill="var(--navy)"/><path d="M12 0h4L10 27H6z" fill="#fff"/></svg>
    <span class="card__url">www.dorvenpartners.example</span>
  </div>
</section>

<!-- Business card, front variant -->
<section class="card card--front card--b">
  <div class="card__brand">
    <div class="mark-dot"></div>
    <div class="wordmark"><span class="line">DORVEN</span><span class="line">PARTNERS</span></div>
  </div>
  <div class="card__divider"></div>
  <div class="card__person">
    <div class="card__name">Ravindra Kohli</div>
    <div class="card__title">Managing Partner</div>
    <div>214 Lantern Avenue, 12th Floor</div>
    <div>Boston, MA 02187</div>
    <div class="card__gap">Phone +1 617 555 0142</div>
    <div>Fax +1 617 555 0143</div>
    <div>Email rkohli@dorvenpartners.example</div>
  </div>
  <div class="card__band">
    <svg class="card__slashes" width="20" height="27" viewBox="0 0 20 27" aria-hidden="true"><path d="M4 0h5L3 27H-2z" fill="var(--navy)"/><path d="M12 0h4L10 27H6z" fill="#fff"/></svg>
    <span class="card__url">www.dorvenpartners.example</span>
  </div>
</section>

<!-- Business card, back -->
<section class="card card--back">
  <div class="faint"></div>
  <div class="back-brand"><div class="mark-dot"></div></div>
  <div class="url">www.dorvenpartners.example</div>
</section>

<!-- Letterhead -->
<div class="sheet sheet--under"></div>
<section class="sheet letterhead">
  <div class="letterhead__brand">
    <div class="mark-dot"></div>
    <div class="wordmark"><span class="line">DORVEN</span><span class="line">PARTNERS</span></div>
  </div>
  <div class="letterhead__contact">
    <div>214 Lantern Avenue, 12th Floor</div>
    <div>Boston, MA 02187</div>
    <div>Phone +1 617 555 0142</div>
    <div>Fax +1 617 555 0143</div>
  </div>
  <div class="faint"></div>
  <div class="letterhead__foot">www.dorvenpartners.example</div>
</section>

<!-- Envelope, back with flap -->
<section class="envelope-back">
  <svg width="420" height="168" viewBox="0 0 420 168" aria-hidden="true">
    <path d="M0 0H420V40Q210 120 0 40Z" fill="var(--navy)"/>
  </svg>
  <div class="mark-dot"></div>
</section>

<!-- Envelope, front -->
<section class="envelope">
  <div class="faint"></div>
  <div class="envelope__brand">
    <div class="mark-dot"></div>
    <div class="wordmark"><span class="line">DORVEN</span><span class="line">PARTNERS</span></div>
  </div>
  <div class="envelope__address">214 Lantern Avenue, 12th Floor Boston, MA 02187</div>
  <div class="envelope__foot">www.dorvenpartners.example</div>
</section>

</body>
</html>
```